Business cards for Volibra employment termination service
Volibra
Wow! I am overwhelmed by how good these all look! It is very difficult to eliminate or rate any of them--they all look great!
Hello: Not sure what happened, but we need to also have "Bismarck, ND 58719" under the PO Box number.
Thanks,
RJD

```html
<!DOCTYPE html>
<html lang="en">
<head>
<meta charset="utf-8">
<title>Volibra Business Card</title>
<link href="https://fonts.googleapis.com/css2?family=Questrial&display=swap" rel="stylesheet">
<style>
  :root {
    --backdrop: #e9e4dc;
    --card-white: #ffffff;
    --teal: #42bfb1;
    --orange: #f6a320;
    --ink-light: #ffffff;
    --tagline-grey: #8a8a8a;
  }
  * { margin: 0; padding: 0; box-sizing: border-box; }
  html, body {
    width: 1200px;
    height: 770px;
    overflow: hidden;
    background: var(--backdrop);
    font-family: "Questrial", "Century Gothic", sans-serif;
  }
  .business-card {
    position: absolute;
    left: 75px;
    top: 85px;
    width: 1050px;
    height: 600px;
    background: var(--card-white);
    box-shadow: 0 6px 18px rgba(0,0,0,0.18);
    overflow: hidden;
  }
  .card-shapes {
    position: absolute;
    inset: 0;
  }
  .brand-lockup {
    position: absolute;
    left: 120px;
    top: 235px;
    width: 400px;
  }
  .brand-row {
    display: flex;
    align-items: center;
    gap: 22px;
  }
  .brand-square {
    width: 62px;
    height: 62px;
    background: var(--orange);
  }
  .brand-name {
    font-size: 62px;
    color: var(--teal);
    letter-spacing: 0.5px;
    line-height: 1;
  }
  .brand-tagline {
    display: flex;
    align-items: center;
    gap: 8px;
    margin-top: 12px;
    margin-left: 84px;
    font-size: 11px;
    letter-spacing: 1.4px;
    color: var(--tagline-grey);
    text-transform: uppercase;
    white-space: nowrap;
  }
  .brand-tagline::before,
  .brand-tagline::after {
    content: "";
    flex: 0 0 14px;
    height: 1px;
    background: var(--tagline-grey);
  }
  .contact-block {
    position: absolute;
    left: 658px;
    top: 122px;
    color: var(--ink-light);
  }
  .person-name {
    font-size: 36px;
    letter-spacing: 0.5px;
    line-height: 1.1;
  }
  .person-title {
    font-size: 30px;
    line-height: 1.2;
  }
  .postal-address {
    margin-top: 52px;
    font-size: 29px;
    line-height: 1.35;
    font-style: normal;
  }
  .contact-list {
    list-style: none;
    margin-top: 30px;
    font-size: 27px;
  }
  .contact-list li {
    display: flex;
    align-items: center;
    gap: 18px;
    height: 39px;
  }
  .contact-icon {
    width: 18px;
    height: 18px;
    flex: 0 0 18px;
  }
</style>
</head>
<body>
  <div class="business-card">
    <svg class="card-shapes" width="1050" height="600" viewBox="0 0 1050 600" aria-hidden="true">
      <rect x="0" y="0" width="1050" height="600" fill="var(--teal)"/>
      <path d="M0 0 H545 C600 170 615 400 572 600 H0 Z" fill="var(--orange)"/>
      <path d="M0 0 H533 C586 170 598 400 550 600 H0 Z" fill="var(--card-white)"/>
    </svg>

    <div class="brand-lockup">
      <div class="brand-row">
        <div class="brand-square"></div>
        <div class="brand-name">Volibra</div>
      </div>
      <div class="brand-tagline">An Employment Termination Service</div>
    </div>

    <div class="contact-block">
      <div class="person-name">DANIEL ROSWELL</div>
      <div class="person-title">CEO</div>
      <address class="postal-address">
        PO Box 2846<br>
        Bismarck, ND 58719
      </address>
      <ul class="contact-list">
        <li>
          <svg class="contact-icon" viewBox="0 0 18 18" aria-hidden="true">
            <circle cx="9" cy="9" r="8" fill="none" stroke="#fff" stroke-width="1.6"/>
            <path d="M6 5 L7.5 5 L8.3 7.3 L7.2 8.2 C7.8 9.5 8.6 10.3 9.8 10.9 L10.7 9.8 L13 10.6 L13 12 C9 12.5 5.6 9 6 5 Z" fill="#fff"/>
          </svg>
          701-555-0143
        </li>
        <li>
          <svg class="contact-icon" viewBox="0 0 18 18" aria-hidden="true">
            <rect x="1" y="4" width="16" height="11" rx="1" fill="#fff"/>
            <path d="M1.5 4.5 L9 10 L16.5 4.5" fill="none" stroke="var(--teal)" stroke-width="1.4"/>
          </svg>
          droswell@volibra.com
        </li>
        <li>
          <svg class="contact-icon" viewBox="0 0 18 18" aria-hidden="true">
            <circle cx="9" cy="9" r="7.5" fill="#fff"/>
            <path d="M1.5 9 H16.5 M9 1.5 C5.5 5 5.5 13 9 16.5 M9 1.5 C12.5 5 12.5 13 9 16.5" fill="none" stroke="var(--teal)" stroke-width="1.2"/>
          </svg>
          www.volibra.com
        </li>
      </ul>
    </div>
  </div>
</body>
</html>
```